Brimford Accounting A5 flyer design

I need a flyer for a new company called Brimford Accounting. I am a self employed accountant and I provide the following services:VAT, Bookeeping, Personal Income Tax, Business Income Tax, Financial Accounting and Accounts Preparation.I am licenced by the GBL and need to include their logo and a statement, this is attached below.The licence wording has to be 8pt Arial Regular and the logo has to be 20mm.The kind of clients I want to attract are self employed traders and partnerships.

Target Market(s)

Self employed traders & partnerships

Industry/Entity Type

Accounting

Requirements
Must have
• Must have GBL logo & licence wording as attached

```html
<!DOCTYPE html>
<html lang="en">
<head>
<meta charset="utf-8">
<title>Brimford Accounting – A5 Flyer</title>
<link rel="stylesheet" href="https://fonts.googleapis.com/css2?family=Oswald:wght@400;500&family=Open+Sans:wght@400;600;700&display=swap">
<style>
  :root {
    --navy: #1e2f63;
    --band-blue: #2e5496;
    --band-navy: #1f3366;
    --tick-blue: #3a5fa8;
    --call-blue: #c4e3f3;
    --ink: #111111;
    --brand-green: #1aa64a;
    --white: #ffffff;
    --photo-light: #eef2f8;
    --photo-mid: #b9c6dc;
    --photo-dark: #5a6f98;
  }
  * { margin: 0; padding: 0; box-sizing: border-box; }
  html, body { width: 1200px; height: 960px; overflow: hidden; background: var(--white); }
  .flyer { position: relative; width: 1200px; height: 960px; background: var(--white); overflow: hidden; }

  .hero-photo {
    position: absolute; left: 426px; top: 0; width: 774px; height: 556px;
    background:
      linear-gradient(90deg, var(--white) 0%, rgba(255,255,255,0) 35%),
      linear-gradient(160deg, var(--photo-light) 0%, var(--photo-mid) 45%, var(--photo-dark) 100%);
  }

  .brand-title {
    position: absolute; left: 96px; top: 40px;
    font-family: "Oswald", sans-serif; font-weight: 500; font-size: 72px;
    letter-spacing: -1px; color: var(--navy); line-height: 1.2;
  }
  .services-heading {
    position: absolute; left: 97px; top: 168px;
    font-family: "Open Sans", sans-serif; font-weight: 700; font-size: 31px; color: var(--ink);
  }
  .services-list {
    position: absolute; left: 97px; top: 228px; list-style: none;
    font-family: "Open Sans", sans-serif; font-size: 31px; color: var(--ink); line-height: 46px;
  }
  .services-list li { display: flex; align-items: center; gap: 11px; }
  .services-list svg { width: 25px; height: 25px; flex: none; }

  .band-tagline { position: absolute; left: 0; top: 556px; width: 1200px; height: 145px; background: var(--band-blue); }
  .band-call { position: absolute; left: 0; top: 715px; width: 1200px; height: 69px; background: var(--band-navy); }

  .tagline {
    position: absolute; left: 440px; top: 566px; width: 724px; text-align: center;
    font-family: "Oswald", sans-serif; font-weight: 400; font-size: 44px; line-height: 56px; color: var(--white);
  }
  .call-line {
    position: absolute; left: 440px; top: 715px; width: 724px; height: 69px;
    display: flex; justify-content: center; align-items: center; gap: 24px;
    font-family: "Oswald", sans-serif; font-weight: 500; font-size: 42px; color: var(--white);
  }
  .call-line .call-label { color: var(--call-blue); letter-spacing: 3px; }

  .trader-photo {
    position: absolute; left: 45px; top: 547px; width: 370px; height: 370px; border-radius: 50%;
    border: 8px solid var(--navy);
    background: radial-gradient(circle at 45% 40%, #f4f6f9 0%, #d6dce6 55%, #8e9ab0 100%);
  }

  .licence-mark {
    position: absolute; left: 612px; top: 846px;
    font-family: "Open Sans", sans-serif; font-weight: 600; font-size: 64px; line-height: 1;
    color: var(--brand-green);
  }
  .licence-text {
    position: absolute; left: 745px; top: 846px; width: 437px;
    font-family: Arial, Helvetica, sans-serif; font-size: 14.5px; line-height: 19.5px;
    color: var(--ink); text-align: justify; text-align-last: right;
  }
</style>
</head>
<body>
<main class="flyer">
  <div class="hero-photo" role="img" aria-label="Photo of an accountant turning ledger pages beside a calculator, pen in hand"></div>

  <h1 class="brand-title">Brimford Accounting</h1>

  <h2 class="services-heading">Services:</h2>
  <ul class="services-list">
    <li><svg viewBox="0 0 24 24" aria-hidden="true"><path d="M20 11.5A8.5 8.5 0 1 1 15.5 4" fill="none" stroke="var(--tick-blue)" stroke-width="2.4" stroke-linecap="round"/><path d="M7.5 11.5l3.5 3.5 8.5-9" fill="none" stroke="var(--tick-blue)" stroke-width="2.4" stroke-linecap="round" stroke-linejoin="round"/></svg>VAT</li>
    <li><svg viewBox="0 0 24 24" aria-hidden="true"><path d="M20 11.5A8.5 8.5 0 1 1 15.5 4" fill="none" stroke="var(--tick-blue)" stroke-width="2.4" stroke-linecap="round"/><path d="M7.5 11.5l3.5 3.5 8.5-9" fill="none" stroke="var(--tick-blue)" stroke-width="2.4" stroke-linecap="round" stroke-linejoin="round"/></svg>Bookeeping</li>
    <li><svg viewBox="0 0 24 24" aria-hidden="true"><path d="M20 11.5A8.5 8.5 0 1 1 15.5 4" fill="none" stroke="var(--tick-blue)" stroke-width="2.4" stroke-linecap="round"/><path d="M7.5 11.5l3.5 3.5 8.5-9" fill="none" stroke="var(--tick-blue)" stroke-width="2.4" stroke-linecap="round" stroke-linejoin="round"/></svg>Personal Income Tax</li>
    <li><svg viewBox="0 0 24 24" aria-hidden="true"><path d="M20 11.5A8.5 8.5 0 1 1 15.5 4" fill="none" stroke="var(--tick-blue)" stroke-width="2.4" stroke-linecap="round"/><path d="M7.5 11.5l3.5 3.5 8.5-9" fill="none" stroke="var(--tick-blue)" stroke-width="2.4" stroke-linecap="round" stroke-linejoin="round"/></svg>Business Income Tax</li>
    <li><svg viewBox="0 0 24 24" aria-hidden="true"><path d="M20 11.5A8.5 8.5 0 1 1 15.5 4" fill="none" stroke="var(--tick-blue)" stroke-width="2.4" stroke-linecap="round"/><path d="M7.5 11.5l3.5 3.5 8.5-9" fill="none" stroke="var(--tick-blue)" stroke-width="2.4" stroke-linecap="round" stroke-linejoin="round"/></svg>Financial Accounting</li>
    <li><svg viewBox="0 0 24 24" aria-hidden="true"><path d="M20 11.5A8.5 8.5 0 1 1 15.5 4" fill="none" stroke="var(--tick-blue)" stroke-width="2.4" stroke-linecap="round"/><path d="M7.5 11.5l3.5 3.5 8.5-9" fill="none" stroke="var(--tick-blue)" stroke-width="2.4" stroke-linecap="round" stroke-linejoin="round"/></svg>Accounts Preparation</li>
  </ul>

  <div class="band-tagline"></div>
  <div class="band-call"></div>

  <p class="tagline">I look after your accounts<br>while you look after your business.</p>
  <p class="call-line"><span class="call-label">CALL</span><span class="call-number">0115 496 0732</span></p>

  <div class="trader-photo" role="img" aria-label="Photo of a trader seen from behind, working at a desk of market chart monitors"></div>

  <p class="licence-mark">GBL</p>
  <p class="licence-text">Dana Rowcliffe is licensed and regulated by GBL under licence number 2004817. GBL is recognised by the National Exchequer to supervise compliance with the Money Laundering Regulations and Brimford Accounting is supervised by GBL in this respect.</p>
</main>
</body>
</html>
```